VantoraCareRX supplement bottle design

We need to redesign our artwork for our line of supplements that is fresh and informative. There are certain design parameters that must be followed for size and content. I will attached our latest design. We want to change our fat metabolizer to fat burner and Gi Stabilizer to Colon Cleanse. The Gi Stabilizer file was too large to upload. The rest stay the same. Here is a link to website www.vantoracarerx.com.

Industry/Entity Type

Health And Wellness

Requirements
Must have
• All disclaimers and who it is produced for
Nice to have
• Fresh look and proper information

```html
<!DOCTYPE html>
<html lang="en">
<head>
<meta charset="utf-8">
<title>VantoraCareRX Calcium Blend Label</title>
<link href="https://fonts.googleapis.com/css2?family=Comfortaa:wght@400;500&family=Marcellus&family=Cinzel:wght@600&display=swap" rel="stylesheet">
<style>
  :root {
    --purple: #6f3f93;
    --purple-text: #7a3f99;
    --sky-light: #d3ecf8;
    --sky-mid: #9fd0ef;
    --sky-deep: #3fa2e3;
    --ink: #141414;
    --white: #ffffff;
    --page: #ffffff;
  }
  * { box-sizing: border-box; margin: 0; padding: 0; }
  html, body { width: 963px; height: 1200px; overflow: hidden; background: var(--page); }
  .canvas { position: relative; width: 963px; height: 1200px; }

  .label {
    position: absolute; left: 20px; top: 408px; width: 923px; height: 383px;
    overflow: hidden;
    font-family: "Comfortaa", sans-serif; color: var(--ink);
  }
  .label-background {
    position: absolute; inset: 0;
    background: linear-gradient(115deg, var(--sky-light) 0%, #bfe2f5 35%, var(--sky-mid) 65%, var(--sky-deep) 100%);
  }
  .band-top, .band-bottom { position: absolute; left: 0; width: 100%; background: var(--purple); }
  .band-top { top: 0; height: 7px; }
  .band-bottom { bottom: 0; height: 7px; }
  .tab-top {
    position: absolute; left: 324px; top: 0; width: 213px; height: 51px;
    background: var(--purple); border-radius: 0 0 26px 26px;
  }
  .tab-count {
    position: absolute; left: 387px; top: 343px; width: 141px; height: 34px;
    background: var(--purple); border-radius: 17px 17px 0 0;
    color: var(--white); font-size: 21px; text-align: center; line-height: 36px;
  }

  .usage { position: absolute; left: 25px; top: 30px; width: 212px; font-size: 11.3px; line-height: 15.3px; }
  .usage h3, .ingredients h3 {
    font-family: "Cinzel", serif; font-weight: 600; font-size: 11px; letter-spacing: .2px; margin-bottom: 1px;
  }
  .usage .caution { margin-top: 14px; }
  .disclaimer {
    position: absolute; left: 18px; top: 283px; width: 211px; height: 84px;
    border: 1px solid #333; padding: 2px 5px; font-size: 11.3px; line-height: 15.3px;
  }

  .centre { position: absolute; left: 300px; width: 323px; text-align: center; color: var(--purple-text); }
  .brand { top: 82px; font-size: 33px; font-weight: 500; letter-spacing: -.5px; }
  .product { top: 166px; font-size: 36px; font-weight: 500; }
  .strength { top: 213px; font-size: 21px; }
  .divider {
    position: absolute; left: 321px; top: 245px; width: 282px; height: 19px;
    background: var(--purple); border-radius: 10px;
  }
  .claim { font-size: 21px; }
  .claim-one { top: 277px; }
  .claim-two { top: 306px; }

  .facts {
    position: absolute; left: 695px; top: 37px; width: 216px; height: 121px;
    background: var(--white); border: 1.5px solid var(--ink); padding: 3px 8px 0;
    font-size: 10.5px; line-height: 15px;
  }
  .facts h2 { font-family: "Marcellus", serif; font-weight: 400; font-size: 21px; line-height: 24px; }
  .facts .row { border-top: 1px solid var(--ink); display: flex; justify-content: space-between; }
  .facts .row.thick { border-top-width: 2px; }
  .facts .plain { border: none; }
  .facts .value { font-size: 8px; }

  .ingredients { position: absolute; left: 688px; top: 172px; width: 218px; font-size: 11.3px; line-height: 15.3px; }
  .ingredients h3 { font-family: "Marcellus", serif; font-weight: 400; font-size: 12px; }
  .storage { position: absolute; left: 688px; top: 299px; width: 200px; font-size: 10.8px; line-height: 15.3px; text-transform: uppercase; }
</style>
</head>
<body>
<div class="canvas">
  <section class="label">
    <div class="label-background" role="img" aria-label="Soft blue geometric triangle background"></div>
    <div class="band-top"></div>
    <div class="tab-top"></div>

    <div class="usage">
      <h3>SUGGESTED USE:</h3>
      <p>1 tablet taken 1 to 4 times daily preferably with a meal or as directed by a healthcare professional</p>
      <h3 class="caution">CAUTION:</h3>
      <p>Do not exceed recommended dose. pregnant or nursing mothers, children under 18, and individuals with a know medical condition any dietry supplement. This product is manufactured and packaged in facility which may also process milk, soy, wheat, egg, peanuts, tree nuts, fish and crustacean shellfish.</p>
    </div>
    <p class="disclaimer">These statements have not beeen evaluated by the food and drug administration. This product is not intended to diagnose, treat, cure, or prevent any disease.</p>

    <p class="centre brand">VantoraCareRX</p>
    <h1 class="centre product">Calcium Blend</h1>
    <p class="centre strength">with 250 IU vitmin D-3</p>
    <div class="divider"></div>
    <p class="centre claim claim-one">Non-GMO Formula</p>
    <p class="centre claim claim-two">Dietary Supplement</p>

    <div class="facts">
      <h2>Supplement Facts</h2>
      <div class="row plain">Serving Size 1 tablet</div>
      <div class="row">Serving Per Container: 60</div>
      <div class="row thick">Amount Per Serving / Daily Value</div>
      <div class="row thick"><span>Vitamin D-3 (cholecalciferol)</span><span class="value">250 IU 63%</span></div>
      <div class="row"><span>Calcium (Carbonate)</span><span class="value">250mg 25%</span></div>
    </div>

    <div class="ingredients">
      <h3>Other Ingredients:</h3>
      <p>Microcrystalline cellulose, acid aqueous clear film coat (HPMC, PEG and purified water), vegetable magnesium stearate and silicon dioxide.</p>
    </div>
    <p class="storage">Keep out of the reach of children. Do not use if safety seal is damaged or missing. Store in cool, dry place.</p>

    <div class="tab-count">60 tablets</div>
    <div class="band-bottom"></div>
  </section>
</div>
</body>
</html>
```